依頼詳細
看板デザインを依頼させて頂きます。看板は国道沿い(店前向かいに設置予定です。看板から「入りやすさ」「高級感」「やわらかさ」が伝わるイメージがあると嬉しいです。
昔ながらの寿司屋の厳ついイメージを払しょくし、且つ安い回転寿司のイメージでもありません。それ相応の高級かつ入りやすい感じが希望です。
記載項目
(例)
会社名:桐葉寿司(家紋入り)
キャッチコピー:駐車場
看板サイズ:横 180㎝ x 縦 545㎝ /横 360㎝×縦123㎝
看板は2種類あり、縦でも横でも使用できるデザインを希望します。
希望イメージ
シンプル 複雑
単色 カラフル
暗い 明るい
日常 高級
遊び心 厳粛
未来的 伝統的
女性的 男性的
希望する色
バックを単色にする場合は、白か青でお願いします。単色以外なら複数色可能です。
納品ファイル
• 高解像度JPG (.jpg)
• イラストレーター形式 (.ai)
補足説明
昼夜問わず使用するので、夜でも目立つものを希望。
遠くからもわかるよう文字サイズは大きめを希望。
大漁旗みたいなデザインは希望せず、シンプルかつおしゃれな感じを希望。
家紋は必ず入れてください。
駐車場全体のイメージを添付しました。
看板のサイズ(2種類)のイメージを添付しました。
店内のイメージを添付しました。
現在の看板と家紋のデータです。
家紋は○の中に二が入っているやつです。
■ 選んだ理由

シンプル且つバランスのよいデザインが気に入りました。
色使いや文字のレイアウトのデザインも気に入りました。
社内選定の結果、こちらの提案を採用させて頂くことになりました。

■ 提案者全員のお礼・コメント

たくさんの素晴らしい提案をいただきありがとうございました。
今回は、初めての仕事依頼で若干の不安もありましたが、それを打ち消すような素晴らしい提案をしてくださった事に、感謝申し上げます。

```html
<!DOCTYPE html>
<html lang="ja">
<head>
<meta charset="utf-8">
<title>桐葉寿司 駐車場 看板</title>
<link rel="stylesheet" href="https://fonts.googleapis.com/css2?family=Dela+Gothic+One&family=Noto+Sans+JP:wght@900&display=swap">
<style>
  :root {
    --page: #ffffff;
    --frame: #9a9a9a;
    --crimson: #7b1519;
    --leaf: #c8dc4a;
    --leaf-soft: #eef4c4;
    --white: #ffffff;
  }
  html, body {
    margin: 0;
    padding: 0;
    width: 1200px;
    height: 1200px;
    overflow: hidden;
    background: var(--page);
  }
  .canvas {
    position: relative;
    width: 1200px;
    height: 1200px;
  }
  .signboard {
    position: absolute;
    left: 414px;
    top: 58px;
    width: 372px;
    height: 1082px;
    box-sizing: border-box;
    border: 7px solid var(--frame);
    background: var(--white);
  }
  .crest {
    position: absolute;
    left: 108px;
    top: 64px;
    width: 142px;
    height: 142px;
  }
  .floral {
    position: absolute;
    left: 5px;
    top: 545px;
    width: 340px;
    height: 420px;
    background: radial-gradient(ellipse at 55% 60%, var(--leaf) 0%, var(--leaf-soft) 55%, rgba(255,255,255,0) 75%);
    opacity: 0.75;
  }
  .shop-name {
    position: absolute;
    left: 0;
    right: 0;
    top: 272px;
    margin: 0;
    writing-mode: vertical-rl;
    text-orientation: upright;
    font-family: "Dela Gothic One", "Noto Sans JP", sans-serif;
    font-weight: 400;
    font-size: 128px;
    line-height: 1;
    letter-spacing: 2px;
    color: var(--crimson);
    display: flex;
    align-items: center;
    margin-left: auto;
    margin-right: auto;
    width: 140px;
  }
  .parking-band {
    position: absolute;
    left: 5px;
    right: 5px;
    bottom: 5px;
    height: 96px;
    background: var(--crimson);
    display: flex;
    align-items: center;
    justify-content: center;
  }
  .parking-label {
    font-family: "Noto Sans JP", sans-serif;
    font-weight: 900;
    font-size: 52px;
    letter-spacing: 2px;
    color: var(--white);
  }
</style>
</head>
<body>
  <main class="canvas">
    <section class="signboard">
      <svg class="crest" viewBox="0 0 142 142" aria-hidden="true">
        <circle cx="71" cy="71" r="71" fill="var(--crimson)"/>
      </svg>
      <div class="floral" role="img" aria-label="淡い黄緑の草花の蔓模様"></div>
      <h1 class="shop-name">桐葉寿司</h1>
      <div class="parking-band">
        <span class="parking-label">駐車場</span>
      </div>
    </section>
  </main>
</body>
</html>
```